Wellspring Care Alliance Vonzo Ads

We want an ad created for the gay dating app vonzo. The size is 300x250. We want the ad to be sexy, with a shirtless man. We are advertising our free HIV and PrEP services. We are open to slogans about maybe "Bringing HIV and PrEP To You"
"Free PrEP and HIV Management"
Open to ideas.

We also offer through the Harborlight Support Fund
Copay Assistance, Insurance Premium Assistance, Free Medical Services, etc
Our website is wcanj.org

I do want the ad to have a Book Now Button

Gay sexually active males

```html
<!DOCTYPE html>
<html lang="en">
<head>
<meta charset="utf-8">
<title>Wellspring Care Alliance – Free PrEP and HIV Management</title>
<link rel="stylesheet" href="https://fonts.googleapis.com/css2?family=Bebas+Neue&family=Great+Vibes&family=Montserrat:wght@700;800;900&display=swap">
<style>
  :root {
    --stage: #808080;
    --white: #ffffff;
    --ink: #111111;
    --wood-dark: #4a3524;
    --wood-mid: #8a6646;
    --wood-light: #b08a62;
    --skin-light: #d9a47f;
    --skin-dark: #9c6a4c;
    --blue: #2f5bf0;
    --violet: #8b3ee0;
    --pink: #ee3fb0;
    --coral: #ff6a4a;
    --copay: #2c63e6;
    --premium: #9b3fd8;
    --medical: #e8436a;
  }
  * { margin: 0; padding: 0; box-sizing: border-box; }
  html, body { width: 1200px; height: 1034px; overflow: hidden; background: var(--stage); }
  .ad {
    position: absolute; left: 100px; top: 100px; width: 1000px; height: 832px;
    background: var(--white); overflow: hidden;
  }
  .ad__backdrop {
    position: absolute; left: 0; top: 0; width: 1000px; height: 698px;
    background: linear-gradient(180deg, var(--wood-mid) 0%, var(--wood-dark) 35%, var(--wood-light) 60%, var(--wood-dark) 100%);
  }
  .ad__model {
    position: absolute; left: 580px; top: 52px; width: 420px; height: 646px;
    background: radial-gradient(ellipse at 50% 45%, var(--skin-light) 0%, var(--skin-dark) 60%, rgba(156,106,76,0) 75%);
  }
  .ad__stripe {
    position: absolute; left: 0; top: 696px; width: 1000px; height: 10px;
    background: linear-gradient(90deg, var(--blue), var(--violet), var(--pink), var(--coral));
  }
  .headline { position: absolute; left: 0; top: 0; }
  .offer {
    position: absolute; left: 58px; top: 404px;
    font-family: "Bebas Neue", "Oswald", sans-serif; font-size: 42px; line-height: 48px;
    color: var(--white); letter-spacing: 0.5px;
  }
  .benefits { position: absolute; left: 0; top: 0; }
  .benefit-label {
    position: absolute; top: 622px; width: 220px; text-align: center;
    font-family: "Bebas Neue", "Oswald", sans-serif; font-size: 34px; line-height: 30px; color: var(--white);
  }
  .book-now { position: absolute; left: 0; top: 0; }
  .book-now__top {
    position: absolute; left: 704px; top: 612px; width: 224px; height: 60px; background: var(--ink);
    font-family: "Montserrat", sans-serif; font-weight: 900; font-size: 52px; line-height: 60px;
    color: var(--white); text-align: center; letter-spacing: 2px;
  }
  .book-now__bottom {
    position: absolute; left: 700px; top: 666px; width: 300px; text-align: center;
    font-family: "Montserrat", sans-serif; font-weight: 900; font-size: 72px; line-height: 90px; color: var(--white);
  }
  .brand {
    position: absolute; left: 60px; top: 738px; width: 250px; display: flex; align-items: center; gap: 12px;
  }
  .brand__dot { width: 44px; height: 44px; border-radius: 50%; background: var(--violet); flex: none; }
  .brand__name {
    font-family: "Montserrat", sans-serif; font-weight: 800; font-size: 24px; line-height: 28px; color: var(--blue);
  }
  .contact { position: absolute; left: 338px; top: 726px; }
  .contact__row { display: flex; align-items: center; gap: 12px; height: 44px;
    font-family: "Montserrat", sans-serif; font-weight: 800; color: var(--ink); }
  .contact__web { font-size: 32px; }
  .contact__phone { font-size: 40px; }
</style>
</head>
<body>
<main class="ad">
  <div class="ad__backdrop" role="img" aria-label="Photograph of stacked weathered wooden planks"></div>
  <div class="ad__model" role="img" aria-label="Photograph of a smiling shirtless man giving a thumbs up"></div>
  <div class="ad__stripe"></div>

  <svg class="headline" width="1000" height="400" viewBox="0 0 1000 400" aria-label="Free PrEP and HIV Management">
    <defs>
      <linearGradient id="neon" x1="0" x2="1" y1="0" y2="0">
        <stop offset="0" stop-color="#3a5cf5"/>
        <stop offset="0.5" stop-color="#a040e8"/>
        <stop offset="1" stop-color="#ff4fa8"/>
      </linearGradient>
      <filter id="glow" x="-10%" y="-10%" width="120%" height="120%">
        <feGaussianBlur stdDeviation="3" result="b"/>
        <feMerge><feMergeNode in="b"/><feMergeNode in="SourceGraphic"/></feMerge>
      </filter>
    </defs>
    <g font-family="Bebas Neue, Oswald, sans-serif" fill="#ffffff" fill-opacity="0.85" stroke="url(#neon)" stroke-width="5" filter="url(#glow)">
      <text x="60" y="284" font-size="350" textLength="364" lengthAdjust="spacingAndGlyphs">FREE</text>
      <text x="444" y="136" font-size="154" textLength="248" lengthAdjust="spacingAndGlyphs" stroke="#ff4fb4">PREP</text>
      <text x="444" y="284" font-size="160" textLength="160" lengthAdjust="spacingAndGlyphs" stroke="#ff4fb4">HIV</text>
      <text x="60" y="376" font-size="106" textLength="524" lengthAdjust="spacingAndGlyphs">MANAGEMENT</text>
    </g>
    <text x="452" y="172" font-family="Great Vibes, cursive" font-size="92" fill="none" stroke="#ff5cc0" stroke-width="2.5" transform="rotate(-14 520 150)">And</text>
  </svg>

  <p class="offer">We also offer through the<br>Harborlight Support Fund</p>

  <svg class="benefits" width="1000" height="700" viewBox="0 0 1000 700">
    <defs>
      <linearGradient id="copay" x1="0" y1="0" x2="1" y2="1"><stop offset="0" stop-color="#2f8cf0"/><stop offset="1" stop-color="#2a3fd0"/></linearGradient>
      <linearGradient id="premium" x1="0" y1="0" x2="1" y2="1"><stop offset="0" stop-color="#6a3ce6"/><stop offset="1" stop-color="#c23fd0"/></linearGradient>
      <linearGradient id="medical" x1="0" y1="0" x2="1" y2="1"><stop offset="0" stop-color="#f0408a"/><stop offset="1" stop-color="#e8503e"/></linearGradient>
    </defs>
    <line x1="170" y1="548" x2="508" y2="548" stroke="#b060e0" stroke-width="3"/>
    <g fill="none" stroke-width="1.5" opacity="0.8">
      <circle cx="112" cy="548" r="70" stroke="#2f6bf0"/>
      <circle cx="310" cy="548" r="70" stroke="#a040e0"/>
      <circle cx="508" cy="548" r="70" stroke="#f0406a"/>
    </g>
    <circle cx="112" cy="548" r="56" fill="url(#copay)"/>
    <circle cx="310" cy="548" r="56" fill="url(#premium)"/>
    <circle cx="508" cy="548" r="56" fill="url(#medical)"/>
    <g fill="#ffffff"><circle cx="112" cy="548" r="45"/><circle cx="310" cy="548" r="45"/><circle cx="508" cy="548" r="45"/></g>
    <g fill="none" stroke="#2c63e6" stroke-width="2.5" stroke-linejoin="round">
      <circle cx="112" cy="532" r="10"/><path d="M112 526v12M106 532h12"/>
      <path d="M92 568v-10h40v10z"/><circle cx="94" cy="548" r="5"/><circle cx="130" cy="548" r="5"/>
    </g>
    <g fill="none" stroke="#9b3fd8" stroke-width="2.5" stroke-linejoin="round">
      <path d="M310 544c-10-12-24-4-18 6l18 14 18-14c6-10-8-18-18-6z"/>
      <path d="M294 548h8l4-6 5 10 4-4h8"/>
      <path d="M288 566l10 6h20l12-8"/>
    </g>
    <g fill="none" stroke="#e8436a" stroke-width="2.5" stroke-linejoin="round">
      <path d="M486 572v-28h44v28z"/><path d="M498 544v-8h20v8"/>
      <path d="M508 552v10M503 557h10"/><path d="M503 572v-6h10v6"/>
      <circle cx="508" cy="528" r="7"/>
    </g>
  </svg>

  <p class="benefit-label" style="left:2px">Copay<br>Assistance</p>
  <p class="benefit-label" style="left:200px">Insurance Premium<br>Assistance</p>
  <p class="benefit-label" style="left:398px">Free Medical<br>Services</p>

  <svg class="book-now" width="1000" height="832" viewBox="0 0 1000 832">
    <defs>
      <linearGradient id="cta" x1="0" x2="1" y1="0" y2="0">
        <stop offset="0" stop-color="#2f6bf0"/><stop offset="0.5" stop-color="#b040e0"/><stop offset="1" stop-color="#ff6a4a"/>
      </linearGradient>
    </defs>
    <path d="M656 654L972 652L962 756H880L814 802L766 756H670Z" fill="url(#cta)"/>
  </svg>
  <div class="book-now__top">BOOK</div>
  <div class="book-now__bottom">NOW!</div>

  <div class="brand">
    <span class="brand__dot"></span>
    <span class="brand__name">Wellspring Care Alliance</span>
  </div>

  <div class="contact">
    <div class="contact__row contact__web">
      <svg width="30" height="30" viewBox="0 0 30 30" aria-hidden="true">
        <circle cx="15" cy="15" r="12" fill="none" stroke="#a040e0" stroke-width="2.5"/>
        <ellipse cx="15" cy="15" rx="5" ry="12" fill="none" stroke="#2f6bf0" stroke-width="2"/>
        <path d="M3 15h24M5 9h20M5 21h20" stroke="#ee3fb0" stroke-width="2"/>
      </svg>
      <span>www.wcanj.org</span>
    </div>
    <div class="contact__row contact__phone">
      <svg width="30" height="30" viewBox="0 0 30 30" aria-hidden="true">
        <path d="M7 3l5 6-3 3c2 4 5 7 9 9l3-3 6 5-3 4C14 27 3 16 3 6z" fill="none" stroke="#ff5a5a" stroke-width="2.5" stroke-linejoin="round"/>
        <path d="M17 5a8 8 0 0 1 8 8M17 10a3 3 0 0 1 3 3" fill="none" stroke="#2f6bf0" stroke-width="2"/>
      </svg>
      <span>201-555-0187</span>
    </div>
  </div>
</main>
</body>
</html>
```